Tour agency for FIT and groups need a business card design

We need a business card design for a tour agency company that is based in Perth called" BRISK NO", we aim to provide customise, unique and seamless travel arrangement for FIT and groups. We serve both high profile businessperson, government authorities, business partners, executives and investors. The name card should be more professional looking.
Updates

Project Deadline Extended Reason: Have some changes that needed to make, director will be back to office on Monday, sorry for the inconvenience cause. Added Saturday, May 6, 2017

Target Market(s)

High profile businessperson, government authorities, business partners, executives and investors.

Industry/Entity Type

Tourism

Contact Information for Business Card

Brisk NO
Level 1, 214 Marlowe Avenue, Dunreath NO, 6120
www.briskno.com.au

Font styles to use
Serif

Colors

Designer to choose colors to be used in the design.

Requirements
Must have
• My project must have a company logo
Nice to have
• a more professional and solid yet friendly name card design. We may want to include chinese name in the name card as well. Edge of the card can be filled with gold and we think that transparent name cards are interesting.

```html
<!DOCTYPE html>
<html lang="en">
<head>
<meta charset="utf-8">
<title>Brisk NO – Business Card</title>
<link href="https://fonts.googleapis.com/css2?family=Crimson+Pro:wght@400;500&display=swap" rel="stylesheet">
<style>
  :root {
    --page: #efefed;
    --card: #ffffff;
    --brand-blue: #1ea6e0;
    --sky: #aee3f7;
    --steel: #8a8c8f;
    --ink: #2b2b2b;
    --muted: #555555;
    --rule: #9a9a9a;
    --icon: #b5b5b5;
    --photo-grey: #9a9a9a;
    --photo-teal: #2f7896;
  }
  * { box-sizing: border-box; margin: 0; padding: 0; }
  html, body { width: 1027px; height: 1200px; overflow: hidden; }
  body {
    background: var(--page);
    font-family: "Crimson Pro", Georgia, serif;
    color: var(--ink);
    position: relative;
  }
  .card {
    position: absolute;
    left: 113px;
    width: 800px;
    height: 457px;
    background: var(--card);
    box-shadow: 0 6px 18px rgba(0,0,0,.18);
    overflow: hidden;
  }
  .card--front { top: 110px; }
  .card--back { top: 640px; }
  .card__art { position: absolute; inset: 0; width: 100%; height: 100%; }

  .front__website {
    position: absolute; left: 70px; bottom: 34px;
    color: #fff; font-size: 24px; letter-spacing: .3px;
  }
  .front__brand {
    position: absolute; left: 450px; top: 150px; width: 300px;
    text-align: center;
    color: var(--brand-blue);
    font-size: 68px; font-weight: 500; line-height: 1;
  }

  .back__identity {
    position: absolute; right: 70px; top: 66px; text-align: right;
  }
  .back__name { font-size: 34px; line-height: 1.1; color: var(--ink); }
  .back__role { font-size: 20px; color: var(--muted); }
  .back__accent {
    position: absolute; right: 20px; top: 62px;
    width: 20px; height: 66px; background: var(--brand-blue);
  }
  .back__rule {
    position: absolute; left: 480px; right: 0; top: 150px;
    height: 1px; background: var(--rule);
  }
  .contact {
    position: absolute; right: 40px; display: flex; align-items: center; gap: 18px;
  }
  .contact__text {
    text-align: right; font-size: 18px; line-height: 1.25; color: var(--ink);
  }
  .contact__icon {
    width: 44px; height: 44px; border-radius: 50%; background: var(--icon);
    display: flex; align-items: center; justify-content: center; flex: none;
  }
  .contact--phone { top: 210px; }
  .contact--web { top: 272px; }
  .contact--address { top: 334px; }
</style>
</head>
<body>

  <section class="card card--front" aria-label="Business card front">
    <svg class="card__art" viewBox="0 0 800 457">
      <defs>
        <linearGradient id="city-tone-front" x1="1" y1="0" x2="0" y2="1">
          <stop offset="0" stop-color="var(--photo-grey)"/>
          <stop offset=".5" stop-color="#6f7d86"/>
          <stop offset="1" stop-color="var(--photo-teal)"/>
        </linearGradient>
      </defs>
      <path role="img" aria-label="City skyline across a river with sailing boats, grey and blue tinted photograph"
            d="M0 0 H250 C380 60 440 200 440 457 H0 Z" fill="url(#city-tone-front)"/>
      <path d="M0 60 C140 200 300 320 440 385" fill="none" stroke="#fff" stroke-width="2"/>
      <path d="M440 345 C500 410 600 445 720 457 H440 Z" fill="var(--sky)"/>
      <path d="M800 60 C770 140 770 290 800 360 Z" fill="var(--steel)"/>
    </svg>
    <p class="front__website">www.briskno.com.au</p>
    <p class="front__brand">Brisk NO</p>
  </section>

  <section class="card card--back" aria-label="Business card back">
    <svg class="card__art" viewBox="0 0 800 457">
      <defs>
        <linearGradient id="city-tone-back" x1="1" y1="0" x2="0" y2="1">
          <stop offset="0" stop-color="var(--photo-grey)"/>
          <stop offset=".5" stop-color="#6f7d86"/>
          <stop offset="1" stop-color="var(--photo-teal)"/>
        </linearGradient>
      </defs>
      <path role="img" aria-label="City skyline across a river with sailing boats, grey and blue tinted photograph"
            d="M0 0 H250 C380 60 440 200 440 457 H0 Z" fill="url(#city-tone-back)"/>
      <path d="M0 60 C140 200 300 320 440 385" fill="none" stroke="#fff" stroke-width="2"/>
      <path d="M440 345 C500 410 600 445 720 457 H440 Z" fill="var(--sky)"/>
    </svg>

    <div class="back__identity">
      <p class="back__name">Loream Ipsum</p>
      <p class="back__role">Travel Consultation</p>
    </div>
    <span class="back__accent"></span>
    <span class="back__rule"></span>

    <div class="contact contact--phone">
      <p class="contact__text">+61 (0)400 555 017<br>00000 00000</p>
      <span class="contact__icon">
        <svg width="22" height="22" viewBox="0 0 24 24" fill="none" stroke="#fff" stroke-width="2" stroke-linecap="round" stroke-linejoin="round">
          <path d="M5 3h4l2 5-3 2a11 11 0 0 0 6 6l2-3 5 2v4a2 2 0 0 1-2 2A17 17 0 0 1 3 5a2 2 0 0 1 2-2z"/>
        </svg>
      </span>
    </div>

    <div class="contact contact--web">
      <p class="contact__text">email@briskno.com<br>www.briskno.com.au</p>
      <span class="contact__icon">
        <svg width="24" height="24" viewBox="0 0 24 24" fill="none" stroke="#fff" stroke-width="1.6">
          <circle cx="12" cy="12" r="9"/>
          <ellipse cx="12" cy="12" rx="4" ry="9"/>
          <path d="M3 12h18M5 7h14M5 17h14"/>
        </svg>
      </span>
    </div>

    <div class="contact contact--address">
      <p class="contact__text">Level 1, 214 Marlowe Avenue,<br>Dunreath NO, 6120</p>
      <span class="contact__icon">
        <svg width="22" height="22" viewBox="0 0 24 24" fill="#fff">
          <path d="M12 2a7 7 0 0 0-7 7c0 5 7 13 7 13s7-8 7-13a7 7 0 0 0-7-7zm0 9.5A2.5 2.5 0 1 1 12 6.5a2.5 2.5 0 0 1 0 5z"/>
        </svg>
      </span>
    </div>
  </section>

</body>
</html>
```